Real Estate Development Company Stationary

We need our company, business card, letterhead, pocket folder and envelope designed.

We are a new real estate development company. We focus on data centre, commercial and real estate development.

Please see attached for our logo. Since it's a new logo, you still can make minor adjust if you like it makes senses

The client has sent me a business card he really likes. Please see file 3.

Target Market(s)

Real Estate Investors
Large corporations
Home buyers

Industry/Entity Type

Real Estate

```html
<!DOCTYPE html>
<html lang="en">
<head>
<meta charset="utf-8">
<title>Velora Development Inc. — Pocket Folder</title>
<link href="https://fonts.googleapis.com/css2?family=Montserrat:wght@400;500;600;700&display=swap" rel="stylesheet">
<style>
  :root {
    --stage: #000000;
    --paper: #ffffff;
    --navy: #0a4487;
    --green: #72bf44;
    --green-dark: #5aa83a;
    --text-grey: #6b6b6b;
    --fold: #8a8a8a;
    --mark-tint: #e9ecf6;
    --label: #ffffff;
  }
  html, body {
    margin: 0;
    padding: 0;
    width: 1200px;
    height: 986px;
    overflow: hidden;
    background: var(--stage);
    font-family: "Montserrat", Arial, sans-serif;
  }
  .canvas {
    position: relative;
    width: 1200px;
    height: 986px;
    background: var(--stage);
  }
  .folder {
    position: absolute;
    left: 22px;
    top: 84px;
    width: 1156px;
    height: 771px;
    background: var(--paper);
    overflow: hidden;
  }
  .folder__fold {
    position: absolute;
    left: 576px;
    top: 0;
    height: 100%;
    border-left: 1.5px dashed var(--fold);
    z-index: 3;
  }
  .folder__band {
    position: absolute;
    left: 0;
    bottom: 0;
    width: 100%;
    height: 38px;
    background: linear-gradient(90deg, var(--navy) 0%, #1a6378 40%, #3f8e63 65%, var(--green) 100%);
  }
  .folder__emblem {
    position: absolute;
    left: 490px;
    top: 316px;
    width: 400px;
    height: 400px;
    z-index: 1;
  }
  .brand {
    position: absolute;
    display: flex;
    align-items: center;
    gap: 8px;
    z-index: 2;
  }
  .brand__dot {
    width: 14px;
    height: 14px;
    border-radius: 50%;
    background: var(--green);
  }
  .brand__name {
    color: var(--green-dark);
    font-weight: 600;
    line-height: 1.05;
    letter-spacing: 0.02em;
  }
  .brand--front {
    right: 22px;
    top: 44px;
  }
  .brand--front .brand__name { font-size: 18px; }
  .brand--back {
    left: 228px;
    top: 612px;
  }
  .brand--back .brand__name { font-size: 13px; }
  .brand--back .brand__dot { width: 11px; height: 11px; }
  .contact {
    position: absolute;
    left: 187px;
    top: 665px;
    width: 200px;
    margin: 0;
    font-style: normal;
    text-align: center;
    color: var(--text-grey);
    font-size: 8.5px;
    line-height: 13.3px;
    z-index: 2;
  }
  .side-label {
    position: absolute;
    top: 880px;
    color: var(--label);
    font-weight: 600;
    font-size: 17px;
    letter-spacing: 0.03em;
    transform: translateX(-50%);
    margin: 0;
  }
  .side-label--back { left: 313px; }
  .side-label--front { left: 886px; }
</style>
</head>
<body>
  <main class="canvas">
    <section class="folder" aria-label="Pocket folder, back and front panels">
      <svg class="folder__emblem" viewBox="0 0 400 400" role="img" aria-label="Large faint brand emblem decoration">
        <circle cx="200" cy="200" r="196" fill="var(--mark-tint)"/>
      </svg>
      <div class="folder__fold" aria-hidden="true"></div>

      <div class="brand brand--front">
        <span class="brand__dot" aria-hidden="true"></span>
        <span class="brand__name">Velora<br>Development Inc.</span>
      </div>

      <div class="brand brand--back">
        <span class="brand__dot" aria-hidden="true"></span>
        <span class="brand__name">Velora<br>Development Inc.</span>
      </div>
      <address class="contact">
        0000 Lakecrest Park Way<br>
        Harbourvale Ontario<br>
        P.O Box 0000, CA<br>
        Tel: (555) 0100-0000
      </address>

      <div class="folder__band" aria-hidden="true"></div>
    </section>

    <p class="side-label side-label--back">BACK</p>
    <p class="side-label side-label--front">FRONT</p>
  </main>
</body>
</html>
```